Design for 3.31” x 84” vinyl banner for tradeshow

Hello, I am looking for a design that will be printed on a 33.31” x 84” vinyl banner for my company’s tradeshow booth.

-Design

My vision: I want to give you the full background, because I think it’ll help. We design insulation for electronic tools that go in high temperature oilwells. Interestingly, a lot of the electronic tools that go down these oil wells are also used in geothermal wells. However the electronics would melt in these high temperature geothermal wells if they were not insulated. A lot of companies that make tools for the oil market are trying to re-purpose their existing tools for the geothermal market…..and to do this, they would need our insulation.

So, our sign needs to conveys this message: Trying to enter the geothermal logging market? it's as simple as increasing the temp. rating for your existing tools

This sign will be placed at our company’s booth at an industry tradeshow. The sign needs to have a similar style to our existing signs. I’ve included images of our booth and all of our other signs. This sign doesn’t have to be identical in artistic style, but be fairly similar.

-Art Requirements:

At least 1 Image of RDP logo

I’ve included several different variations. Use your judgement to select the one that you think is most fitting.

Do not use the portion of the logo that says “40 years”. Feel free to crop that out if you would like.

At least 2 images of logging tools. You can select more than 2 if you think that’s necessary. Logging tools are the long metal tubes.

I’ve included several pictures of different logging tools. I would like to see at least 2 pictures of tools on the banner. Please include the image titled “Full, double centarlizer” It could look cool if this picture extended the full length of the banner (just a suggestion). I purchased these images off of picvault.For the second image of the tool, feel free to include whatever tool you think looks best.

-Colors and font: Like I mentioned above, I would like it to look close to the other signs we have at our booth. Please select colors and fonts that will fit with our other signs.

-Other thoughts/suggestions

When most people in our industry think of geothermal, the automatically associate it with extremely high temperatures. I’m open to seeing warmer colors (orange/red) that help convey this idea.

I’m also open to seeing pictures of geothermal power plants, I included an image of this titled “geothermal” that you may use if you like. This is not mandatory, just a suggestion.

-Text: the main text needs to be: “Trying to enter the Geothermal logging market? Ask us about increasing the temperature rating for your existing tools” No other text is required.

Printing/Art specifications:

I’ll be giving the design I receive off art-hive to a local banner printing shop. I’ve included their printing and art guidelines, please take a look at it and let me know if you have any questions. It’s pretty detailed so I hope it provides you with enough information. The design would have to follow the requirements in the two attached word documents.

Target Market(s)

oil and gas professionals

Industry/Entity Type

oil and gas/geothermal

Font styles to use
Other font styles liked:
• Fonts similar the font used on our other tradeshow signs (images attached)

Colors
F0912C
F2A743
F7CA91
FBE8D2
FDF5EE

Requirements
Must have
• -At least 1 Image of RDP logo, At least 2 images of logging tools (1 of these 2 pictures must be image titled "full double centralizer", he main text needs to be: “Trying to enter the Geothermal logging market? Ask us about increasing the temperature rating for your existing tools” , the design must follow the requirements in the printing and art guideline documents I attached.
Nice to have
• please select colors and fonts that will fit with our other signs.

```html
<!DOCTYPE html>
<html lang="en">
<head>
<meta charset="utf-8">
<title>Geothermal Logging Banner</title>
<link rel="stylesheet" href="https://fonts.googleapis.com/css2?family=Anton&family=Archivo:wght@800&display=swap">
<style>
  :root {
    --stage: #b5b5b5;
    --paper: #ffffff;
    --ink: #111111;
    --orange-deep: #f0912c;
    --orange: #f2a743;
    --orange-soft: #f7ca91;
    --cream: #fbe8d2;
    --cream-light: #fdf5ee;
    --steel-dark: #5b5b5b;
    --steel-light: #c9c9c9;
  }
  * { margin: 0; padding: 0; box-sizing: border-box; }
  html, body { width: 1200px; height: 1200px; overflow: hidden; }
  body { background: var(--stage); position: relative; font-family: "Anton", "Impact", sans-serif; }

  .banner {
    position: absolute; left: 409px; top: 117px;
    width: 382px; height: 966px;
    background: var(--paper); overflow: hidden;
  }
  .banner__waves { position: absolute; inset: 0; }

  .brand {
    position: absolute; top: 30px; left: 0; right: 0;
    display: flex; justify-content: center; align-items: center; gap: 10px;
  }
  .brand__mark { width: 40px; height: 40px; background: var(--ink); }
  .brand__name {
    font-family: "Archivo", "Arial Black", sans-serif; font-weight: 800;
    font-size: 19px; line-height: 1; color: var(--ink); letter-spacing: 0.2px;
  }

  .headline {
    position: absolute; top: 176px; left: 0; right: 0;
    text-align: center; color: var(--ink); text-transform: uppercase;
  }
  .headline__lead { font-size: 29px; line-height: 1.2; display: block; }
  .headline__main { font-size: 46px; line-height: 1.2; display: block; margin-top: 4px; }

  .offer {
    position: absolute; top: 506px; right: 16px;
    text-align: right; color: var(--ink); text-transform: uppercase;
    font-size: 23px; line-height: 36px;
  }
  .offer span { display: block; }

  .tool {
    position: absolute; border-radius: 2px;
    background: linear-gradient(90deg, var(--steel-dark), var(--steel-light) 50%, var(--steel-dark));
  }
  .tool--long { left: 75px; top: 366px; width: 6px; height: 583px; }
  .tool--short { left: 186px; top: 772px; width: 10px; height: 172px; }
</style>
</head>
<body>
  <main class="banner">
    <svg class="banner__waves" viewBox="0 0 382 966" preserveAspectRatio="none" aria-hidden="true">
      <defs>
        <linearGradient id="warm" x1="0" y1="1" x2="0.6" y2="0">
          <stop offset="0" stop-color="var(--orange-deep)"/>
          <stop offset="0.45" stop-color="var(--orange-soft)"/>
          <stop offset="1" stop-color="var(--cream)"/>
        </linearGradient>
      </defs>
      <path d="M0 262 C40 238 120 250 150 320 C175 390 140 470 170 560 C195 620 280 630 320 690 C360 740 382 720 382 700 L382 966 L0 966 Z" fill="var(--cream)"/>
      <path d="M0 350 C40 340 70 330 80 360 C95 420 70 480 120 540 C170 600 230 610 280 650 C330 690 350 760 382 770 L382 966 L0 966 Z" fill="url(#warm)"/>
    </svg>

    <header class="brand">
      <span class="brand__mark"></span>
      <span class="brand__name">REDPINE<br>WORKS, Inc.</span>
    </header>

    <h1 class="headline">
      <span class="headline__lead">Trying to enter the</span>
      <span class="headline__main">Geothermal<br>Logging Market?</span>
    </h1>

    <p class="offer">
      <span>Ask us</span>
      <span>About&nbsp; increasing the</span>
      <span>temperature rating</span>
      <span>for your existing</span>
      <span>tools</span>
    </p>

    <div class="tool tool--long" role="img" aria-label="Photo of a full-length logging tool with double centralizer"></div>
    <div class="tool tool--short" role="img" aria-label="Photo of a short logging tool with centralizer"></div>
  </main>
</body>
</html>
```